Need DL Flyer for Real Estate Drops

We need a real estate flyer ,double sided. With content on 1 side like: Want to know what's your house is worth " contact us today and on other side agent details. We are looking for an ongoing partnership with designer so this assignment will be ongoing

```html
<!DOCTYPE html>
<html lang="en">
<head>
<meta charset="utf-8">
<title>Meridian Real Estate – DL Flyer</title>
<link href="https://fonts.googleapis.com/css2?family=Poppins:wght@400;500;600;700&display=swap" rel="stylesheet">
<style>
  :root{
    --backdrop:#e4ddd4;
    --paper:#ffffff;
    --paper-fade:#eeeef0;
    --navy:#121a33;
    --navy-deep:#0c1226;
    --red:#d4313b;
    --red-deep:#b70b14;
    --white:#ffffff;
    --grass:#5f9a43;
    --roof:#4f6b9a;
    --wall:#dfe4ea;
  }
  *{box-sizing:border-box;margin:0;padding:0}
  html,body{width:1200px;height:900px;overflow:hidden}
  body{
    background:var(--backdrop);
    font-family:"Poppins",sans-serif;
    display:flex;align-items:center;justify-content:center;gap:70px;
  }
  .flyer{
    width:360px;height:756px;position:relative;overflow:hidden;
    box-shadow:0 18px 40px rgba(60,50,40,.22);
  }

  /* Front side */
  .flyer--front{
    background:linear-gradient(180deg,var(--paper) 0%,var(--paper-fade) 70%);
    display:flex;flex-direction:column;
  }
  .front__headline{
    margin:70px 40px 0;
    color:var(--navy);font-weight:700;font-size:30px;line-height:1.15;text-align:center;
  }
  .front__mark{
    text-align:center;color:var(--red);font-weight:700;
    font-size:230px;line-height:1;margin-top:10px;position:relative;z-index:1;
  }
  .front__photo{
    position:absolute;left:0;right:0;top:420px;height:170px;
    background:linear-gradient(180deg,var(--wall) 0%,var(--roof) 45%,var(--grass) 100%);
    opacity:.9;
  }
  .front__band{
    position:absolute;left:0;right:0;bottom:0;height:166px;
    background:linear-gradient(180deg,var(--navy) 0%,var(--navy-deep) 100%);
    display:flex;flex-direction:column;align-items:center;justify-content:center;gap:12px;
  }
  .brand{display:flex;align-items:center;gap:12px;color:var(--white);font-weight:600}
  .brand__square{width:26px;height:26px;background:var(--red)}
  .brand__name{font-size:28px;line-height:1}
  .front__phone{color:var(--white);font-weight:700;font-size:36px;letter-spacing:1px}

  /* Back side */
  .flyer--back{
    background:linear-gradient(180deg,var(--red) 0%,var(--red-deep) 100%);
    color:var(--white);text-align:center;
    display:flex;flex-direction:column;align-items:center;
  }
  .flyer--back .brand{margin-top:64px}
  .flyer--back .brand__square{background:var(--white)}
  .agent__portrait{
    margin-top:50px;width:214px;height:214px;border-radius:50%;
    border:2px solid var(--white);display:flex;align-items:center;justify-content:center;
  }
  .agent__photo{
    width:190px;height:190px;border-radius:50%;
    background:radial-gradient(circle at 50% 40%,#f2f2f2 0%,#bdbdbd 100%);
  }
  .agent__name{margin-top:40px;font-size:38px;font-weight:500;line-height:1.1}
  .agent__role{margin-top:12px;font-size:16px;line-height:1.4}
  .divider{width:64px;height:2px;background:var(--white);opacity:.85;margin:26px auto}
  .agent__contact{font-size:15px;line-height:1.6;list-style:none}
  .agent__address{font-size:15px;line-height:1.5;text-transform:uppercase}
</style>
</head>
<body>

  <section class="flyer flyer--front" aria-label="Flyer front">
    <h1 class="front__headline">Want to know what's your house is worth</h1>
    <div class="front__photo" role="img" aria-label="Photo of a two-storey house with a blue tiled roof on a green lawn"></div>
    <div class="front__mark" aria-hidden="true">?</div>
    <div class="front__band">
      <div class="brand">
        <span class="brand__square"></span>
        <span class="brand__name">Meridian Real Estate</span>
      </div>
      <p class="front__phone">03 9000 1234</p>
    </div>
  </section>

  <section class="flyer flyer--back" aria-label="Flyer back">
    <div class="brand">
      <span class="brand__square"></span>
      <span class="brand__name">Meridian Real Estate</span>
    </div>
    <div class="agent__portrait">
      <div class="agent__photo" role="img" aria-label="Black and white portrait of the agent in a suit"></div>
    </div>
    <h2 class="agent__name">Rohan<br>Mehta</h2>
    <p class="agent__role">Managing Director/LEA,<br>Meridian Real Estate</p>
    <div class="divider"></div>
    <ul class="agent__contact">
      <li>Tel: 03 9000 1234</li>
      <li>Mobile: 0400 000 111</li>
      <li>rohan@meridianrealestate.com.au</li>
    </ul>
    <div class="divider"></div>
    <p class="agent__address">14/8 Harbour Lane,<br>Westfield 3030</p>
  </section>

</body>
</html>
```